Brookmere Osteopathy flyer

I want a clean clear DL flyer (but also want an A4 poster) promoting a new Osteopathic business in a semi rural area in Tasmania (Australia).
It can have pictures like the examples attached to show people what Osteopathy is (its like Chiropractic and physiotherapy).
I am the sole practioner and am male, so any pictures would be best to be a white male if possible.
I've attached some wording, you can use all, or none of it
I don't have a phone number for the business yet
info@brookmereosteopathy.example
www.brookmereosteopathy.example
Target Market(s)
Australians, from tradies, professionals, babies to retired people
Industry/Entity Type
Health
Look and feel

```html
<!DOCTYPE html>
<html lang="en">
<head>
<meta charset="utf-8">
<title>Brookmere Osteopathy – DL Flyer</title>
<link rel="stylesheet" href="https://fonts.googleapis.com/css2?family=Mulish:wght@400;600;700&family=Oswald:wght@500;600&family=Prata&display=swap">
<style>
  :root {
    --blue: #1a8ccc;
    --blue-dark: #1479b3;
    --orange: #f7941d;
    --ink: #2a2a2a;
    --white: #ffffff;
    --ground: #ecebe8;
  }
  * { box-sizing: border-box; margin: 0; padding: 0; }
  html, body { width: 1200px; height: 1094px; overflow: hidden; }
  body { background: var(--ground); font-family: "Mulish", sans-serif; color: var(--ink); position: relative; }

  .panel { position: absolute; top: 79px; width: 440px; height: 936px; background: var(--white); overflow: hidden; box-shadow: 0 2px 8px rgba(0,0,0,.12); }
  .panel--front { left: 200px; }
  .panel--back { left: 674px; }

  /* brand mark */
  .brand { position: absolute; display: flex; align-items: center; gap: 8px; font-family: "Mulish", sans-serif; font-weight: 700; line-height: 1.15; }
  .brand__dot { width: 26px; height: 26px; border-radius: 50%; flex: none; }
  .brand--header { left: 16px; top: 32px; color: var(--blue); font-size: 17px; }
  .brand--header .brand__dot { border: 2px solid var(--blue); }
  .brand--footer { right: 14px; top: 36px; color: var(--white); font-size: 13px; }
  .brand--footer .brand__dot { border: 2px solid var(--white); width: 20px; height: 20px; }

  /* header call */
  .call { position: absolute; display: flex; align-items: center; gap: 12px; }
  .call--header { left: 184px; top: 24px; }
  .call__label { font-size: 14px; font-weight: 600; color: var(--blue); }
  .call__number { font-family: "Prata", serif; font-size: 29px; color: var(--blue); line-height: 1.1; }
  .call--footer { left: 14px; top: 24px; }
  .call--footer .call__label { color: var(--white); font-size: 14px; }
  .call--footer .call__number { font-family: "Oswald", sans-serif; font-weight: 600; color: var(--white); font-size: 30px; }

  /* photos */
  .photo { position: absolute; left: 0; width: 440px; display: block; }
  .photo--front { top: 102px; height: 450px; }
  .photo--back { top: 0; height: 310px; }

  .headline { position: absolute; left: 19px; top: 215px; font-family: "Oswald", sans-serif; font-weight: 600; color: var(--blue); font-size: 42px; line-height: 50px; letter-spacing: .5px; }
  .tagline { position: absolute; left: 17px; top: 360px; font-family: "Oswald", sans-serif; font-weight: 500; color: var(--ink); font-size: 26px; letter-spacing: .5px; }

  .intro { position: absolute; left: 13px; top: 553px; width: 420px; font-size: 12.6px; line-height: 26.2px; }
  .service-area { position: absolute; left: 14px; top: 760px; font-size: 17px; font-weight: 600; }
  .offer { position: absolute; left: 13px; top: 784px; font-family: "Oswald", sans-serif; font-weight: 500; color: var(--blue); font-size: 30px; letter-spacing: .3px; }

  .rule { position: absolute; left: 0; width: 440px; height: 3px; top: 836px; }
  .rule--orange { background: var(--orange); }
  .rule--blue { background: var(--blue); }

  .footer { position: absolute; left: 0; top: 842px; width: 440px; height: 94px; background: var(--blue); }
  .contact { position: absolute; left: 16px; top: 8px; list-style: none; color: var(--white); font-size: 11.2px; font-weight: 600; }
  .contact li { display: flex; align-items: center; gap: 8px; height: 20.5px; }
  .contact svg { width: 12px; height: 12px; flex: none; }

  .reasons-title { position: absolute; left: 21px; top: 318px; font-family: "Mulish", sans-serif; font-weight: 700; color: var(--blue); font-size: 29px; line-height: 35px; }
  .reasons { position: absolute; left: 21px; top: 398px; list-style: none; }
  .reasons li { display: flex; align-items: center; gap: 12px; height: 42px; font-size: 20px; font-weight: 600; color: var(--ink); }
  .reasons svg { width: 18px; height: 12px; flex: none; }
</style>
</head>
<body>

<!-- Front -->
<section class="panel panel--front">
  <div class="brand brand--header"><span class="brand__dot"></span><span>Brookmere<br>Osteopathy</span></div>

  <div class="call call--header">
    <svg width="36" height="40" viewBox="0 0 36 40" fill="none" stroke="var(--orange)" stroke-width="2.2" stroke-linecap="round" stroke-linejoin="round" aria-hidden="true">
      <path d="M8 4 L14 12 L10 16 Q13 24 19 29 L23 25 L30 32 L25 37 Q14 35 6 22 Q2 12 8 4 Z"/>
      <path d="M20 8 Q26 10 27 16"/><path d="M22 2 Q31 5 33 14"/>
    </svg>
    <div>
      <div class="call__label">Visit Us Today</div>
      <div class="call__number">555.014.2260</div>
    </div>
  </div>

  <svg class="photo photo--front" viewBox="0 0 440 450" role="img" aria-label="Photo: practitioner massaging a patient's shoulder and upper back on a treatment table">
    <defs>
      <linearGradient id="frontPhoto" x1="0" y1="0" x2="1" y2="1">
        <stop offset="0" stop-color="#f1ece8"/>
        <stop offset=".45" stop-color="#d9a78a"/>
        <stop offset=".8" stop-color="#c38a6c"/>
        <stop offset="1" stop-color="#e9e4e2"/>
      </linearGradient>
    </defs>
    <path d="M0 0 H440 V382 Q220 488 0 382 Z" fill="url(#frontPhoto)"/>
    <path d="M0 382 Q220 500 440 382 Q220 482 0 382 Z" fill="#2b2b2b"/>
  </svg>

  <h1 class="headline">CHIROPRACTIC<br>AND<br>PHYSIOTHERAPY</h1>
  <p class="tagline">Move Better, Feel Better.</p>

  <p class="intro">Brookmere Osteopathy use a tailored combination of joint mobilisa-tion/manipulation, stretching, movement, trigger point dry needling and targeted massage to reduce pain and restore optimal function. Hands-on treatment is backed up with rehabilitative exercise prescription and advice.<br>So whether you're recovering from injury or managing chronic discomfort, we're here to help you move better and feel your best.</p>

  <p class="service-area">Serving Semi Rural Area In Tasmania - Australia</p>
  <p class="offer">FREE INTIAL PHYSIO CONSULTATION</p>

  <div class="rule rule--orange"></div>
  <footer class="footer">
    <ul class="contact">
      <li><svg viewBox="0 0 12 12" aria-hidden="true"><path d="M6 11 Q1.5 6 1.5 4.5 A4.5 4.5 0 0 1 10.5 4.5 Q10.5 6 6 11 Z" fill="var(--orange)"/><circle cx="6" cy="4.5" r="1.6" fill="var(--blue)"/></svg>48 Millbrook Lane, Brookmere</li>
      <li><svg viewBox="0 0 12 12" aria-hidden="true"><circle cx="6" cy="6" r="5.2" fill="none" stroke="var(--orange)" stroke-width="1"/><path d="M4 3 L5.3 4.6 L4.6 5.4 Q5.4 7 6.6 7.6 L7.4 6.8 L9 8.1 L8 9.1 Q5 8.6 3.2 4.2 Z" fill="var(--orange)"/></svg>555.014.2261</li>
      <li><svg viewBox="0 0 12 12" aria-hidden="true"><rect x="1" y="3" width="10" height="7" fill="none" stroke="var(--orange)" stroke-width="1.2"/><path d="M1 3 L6 7 L11 3" fill="none" stroke="var(--orange)" stroke-width="1.2"/></svg>info@brookmereosteopathy.example</li>
      <li><svg viewBox="0 0 12 12" aria-hidden="true"><circle cx="6" cy="6" r="5" fill="none" stroke="var(--orange)" stroke-width="1"/><ellipse cx="6" cy="6" rx="2.2" ry="5" fill="none" stroke="var(--orange)" stroke-width="1"/><path d="M1 6 H11" stroke="var(--orange)" stroke-width="1"/></svg>www.brookmereosteopathy.example</li>
    </ul>
    <div class="brand brand--footer"><span class="brand__dot"></span><span>Brookmere<br>Osteopathy</span></div>
  </footer>
</section>

<!-- Back -->
<section class="panel panel--back">
  <svg class="photo photo--back" viewBox="0 0 440 310" role="img" aria-label="Photo: practitioner applying hands-on treatment to a patient's lower back as they lie on their side">
    <defs>
      <linearGradient id="backPhoto" x1="0" y1="0" x2="1" y2="1">
        <stop offset="0" stop-color="#e7e1dc"/>
        <stop offset=".3" stop-color="#2e3c5e"/>
        <stop offset=".55" stop-color="#d5a184"/>
        <stop offset=".85" stop-color="#caa08a"/>
        <stop offset="1" stop-color="#f1efee"/>
      </linearGradient>
    </defs>
    <path d="M0 0 H440 V243 Q220 335 0 243 Z" fill="url(#backPhoto)"/>
    <path d="M0 243 Q220 350 440 243 Q220 330 0 243 Z" fill="var(--orange)"/>
  </svg>

  <h2 class="reasons-title">Common Reasons People<br>Visit An Osteopath:</h2>
  <ul class="reasons">
    <li><svg viewBox="0 0 18 12" aria-hidden="true"><path d="M1 11 Q3 4 11 4 L11 1 L17 5.5 L11 10 L11 7 Q5 7 1 11 Z" fill="var(--orange)"/></svg>Back / Neck Pain</li>
    <li><svg viewBox="0 0 18 12" aria-hidden="true"><path d="M1 11 Q3 4 11 4 L11 1 L17 5.5 L11 10 L11 7 Q5 7 1 11 Z" fill="var(--orange)"/></svg>Headaches / Migraines</li>
    <li><svg viewBox="0 0 18 12" aria-hidden="true"><path d="M1 11 Q3 4 11 4 L11 1 L17 5.5 L11 10 L11 7 Q5 7 1 11 Z" fill="var(--orange)"/></svg>Joint And Muscle Pain</li>
    <li><svg viewBox="0 0 18 12" aria-hidden="true"><path d="M1 11 Q3 4 11 4 L11 1 L17 5.5 L11 10 L11 7 Q5 7 1 11 Z" fill="var(--orange)"/></svg>Pregnancy-related Discomfort</li>
    <li><svg viewBox="0 0 18 12" aria-hidden="true"><path d="M1 11 Q3 4 11 4 L11 1 L17 5.5 L11 10 L11 7 Q5 7 1 11 Z" fill="var(--orange)"/></svg>Disc Related Issues</li>
    <li><svg viewBox="0 0 18 12" aria-hidden="true"><path d="M1 11 Q3 4 11 4 L11 1 L17 5.5 L11 10 L11 7 Q5 7 1 11 Z" fill="var(--orange)"/></svg>Sciatica</li>
    <li><svg viewBox="0 0 18 12" aria-hidden="true"><path d="M1 11 Q3 4 11 4 L11 1 L17 5.5 L11 10 L11 7 Q5 7 1 11 Z" fill="var(--orange)"/></svg>Plantar Fasciitis</li>
    <li><svg viewBox="0 0 18 12" aria-hidden="true"><path d="M1 11 Q3 4 11 4 L11 1 L17 5.5 L11 10 L11 7 Q5 7 1 11 Z" fill="var(--orange)"/></svg>Tendonitis / Bursitis</li>
    <li><svg viewBox="0 0 18 12" aria-hidden="true"><path d="M1 11 Q3 4 11 4 L11 1 L17 5.5 L11 10 L11 7 Q5 7 1 11 Z" fill="var(--orange)"/></svg>Adhesive Capsulitis (Frozen Shoulder)</li>
    <li><svg viewBox="0 0 18 12" aria-hidden="true"><path d="M1 11 Q3 4 11 4 L11 1 L17 5.5 L11 10 L11 7 Q5 7 1 11 Z" fill="var(--orange)"/></svg>Tennis / Golfers Elbow</li>
  </ul>

  <div class="rule rule--blue"></div>
  <footer class="footer">
    <div class="call call--footer">
      <svg width="36" height="40" viewBox="0 0 36 40" fill="none" stroke="var(--orange)" stroke-width="2.2" stroke-linecap="round" stroke-linejoin="round" aria-hidden="true">
        <path d="M8 4 L14 12 L10 16 Q13 24 19 29 L23 25 L30 32 L25 37 Q14 35 6 22 Q2 12 8 4 Z"/>
        <path d="M20 8 Q26 10 27 16"/><path d="M22 2 Q31 5 33 14"/>
      </svg>
      <div>
        <div class="call__label">Visit Us Today</div>
        <div class="call__number">555.014.2260</div>
      </div>
    </div>
    <div class="brand brand--footer"><span class="brand__dot"></span><span>Brookmere<br>Osteopathy</span></div>
  </footer>
</section>

</body>
</html>
```